VELOQUARD Stationery Design Project

I want a stationery design for a web development company consists of:
1- business card
2- Letter Head
3- small Envelope
4- Large Envelope

need a very clean professional simple design yet creative,

The company logo is attached
http://www.artpitchly.com/project-progress/designs.aspx?briefId=5173048&submissionId=73920416

logo font is sui generis rg (attached)
I would like to have the stationery text font to be helvetica font regular or light (can be changed)

I love the combination of cyan, black and grey colors
( will attach some recommended styles)

Industry/Entity Type

Business

Requirements
Should not have
• curves or waves

```html
<!DOCTYPE html>
<html lang="en">
<head>
<meta charset="utf-8">
<title>VELOQUARD Stationery</title>
<link href="https://fonts.googleapis.com/css2?family=Michroma&family=Open+Sans:wght@400;600&display=swap" rel="stylesheet">
<style>
  :root {
    --backdrop: #cfcfcf;
    --paper: #ffffff;
    --charcoal: #414141;
    --charcoal-deep: #3a3a3a;
    --charcoal-tint: #4a4a4a;
    --slate: #3e4347;
    --cyan: #27a8e0;
    --cyan-pale: #d6ecf8;
    --grey-pale: #ececec;
    --ink: #333333;
    --shadow: 3px 4px 6px rgba(0,0,0,.45);
  }
  * { box-sizing: border-box; margin: 0; padding: 0; }
  html, body { width: 1200px; height: 1029px; overflow: hidden; }
  body { background: var(--backdrop); position: relative; font-family: "Open Sans", Arial, sans-serif; color: var(--ink); }

  .sheet { position: absolute; box-shadow: var(--shadow); overflow: hidden; }
  .paper { background: var(--paper); }
  .dark { background: var(--charcoal); }

  .brand { position: absolute; display: flex; align-items: center; gap: 6px; white-space: nowrap; }
  .brand-square { background: var(--cyan); flex: none; }
  .brand-name { font-family: "Michroma", "Open Sans", sans-serif; color: var(--cyan); letter-spacing: .12em; line-height: 1; }

  .accent-block { position: absolute; }

  .contact { position: absolute; font-size: 6.6px; line-height: 9px; color: var(--ink); }
  .contact li { list-style: none; display: flex; align-items: center; gap: 4px; }
  .contact svg { width: 5px; height: 5px; flex: none; }
  .address { position: absolute; font-size: 6.6px; line-height: 9px; color: var(--ink); }

  /* letterhead */
  .letterhead { left: 136px; top: 61px; width: 412px; height: 533px; }
  .letterhead .brand { left: 26px; top: 60px; }
  .letterhead .brand-square { width: 12px; height: 12px; }
  .letterhead .brand-name { font-size: 13px; }

  /* folder */
  .folder { left: 583px; top: 62px; width: 405px; height: 535px; }
  .folder .brand { left: 120px; top: 128px; }
  .folder .brand-square { width: 16px; height: 16px; }
  .folder .brand-name { font-size: 17px; }

  /* business cards */
  .card-front { left: 328px; top: 666px; width: 220px; height: 125px; }
  .card-front .brand { left: 13px; top: 39px; }
  .card-front .brand-square { width: 8px; height: 8px; }
  .card-front .brand-name { font-size: 9px; }
  .holder { position: absolute; left: 13px; top: 74px; }
  .holder-name { font-size: 7.4px; font-weight: 600; color: var(--cyan); line-height: 9px; }
  .holder-role { font-size: 5px; line-height: 6px; }
  .card-front .contact, .card-front .address { font-size: 5.2px; line-height: 7px; }
  .card-front .contact { left: 13px; top: 95px; }
  .card-front .address { right: 13px; top: 102px; text-align: right; }

  .card-back { left: 328px; top: 802px; width: 220px; height: 125px; }
  .card-back .brand { left: 66px; top: 60px; }
  .card-back .brand-square { width: 8px; height: 8px; }
  .card-back .brand-name { font-size: 9px; }

  /* envelopes */
  .envelope-back { left: 585px; top: 635px; width: 339px; height: 154px; }
  .envelope-flap { position: absolute; left: 0; top: 0; width: 339px; height: 50px; }
  .envelope-back .brand-square { position: absolute; left: 162px; top: 15px; width: 14px; height: 14px; background: var(--cyan); }

  .envelope-front { left: 585px; top: 804px; width: 339px; height: 154px; }
  .envelope-front .brand { left: 15px; top: 39px; }
  .envelope-front .brand-square { width: 9px; height: 9px; }
  .envelope-front .brand-name { font-size: 10px; }
  .envelope-front .address { left: 15px; top: 129px; font-size: 5.4px; line-height: 8px; }
</style>
</head>
<body>

<section class="sheet paper letterhead" aria-label="Letterhead">
  <div class="brand"><span class="brand-square"></span><span class="brand-name">VELOQUARD</span></div>
  <div class="accent-block" style="left:264px;top:432px;width:148px;height:48px;background:var(--cyan-pale)"></div>
  <div class="accent-block" style="left:264px;top:480px;width:148px;height:53px;background:var(--grey-pale)"></div>
  <ul class="contact" style="left:26px;top:491px">
    <li><svg viewBox="0 0 10 10"><path d="M2 1l2 2-1 1.5c.8 1.5 1.5 2.2 3 3L7.5 6l2 2-1.5 1.5C4 9 1 6 .5 1.5z" fill="var(--cyan)"/></svg>888-8888-8888</li>
    <li><svg viewBox="0 0 10 10"><rect x="0" y="2" width="10" height="6" fill="var(--cyan)"/></svg>info@websitename.com</li>
    <li><svg viewBox="0 0 10 10"><circle cx="5" cy="5" r="4" fill="none" stroke="var(--cyan)" stroke-width="1.4"/></svg>www.websitename.com</li>
  </ul>
  <p class="address" style="left:124px;top:500px">55 demo street, demo place<br>P.O. Box 000, 555 Avenue</p>
</section>

<section class="sheet dark folder" aria-label="Presentation folder">
  <div class="accent-block" style="left:0;top:0;width:405px;height:166px;background:var(--slate)"></div>
  <div class="accent-block" style="left:0;top:166px;width:405px;height:70px;background:var(--charcoal-tint)"></div>
  <div class="brand"><span class="brand-square"></span><span class="brand-name">VELOQUARD</span></div>
</section>

<section class="sheet paper card-front" aria-label="Business card front">
  <div class="accent-block" style="left:128px;top:0;width:92px;height:26px;background:var(--cyan-pale)"></div>
  <div class="accent-block" style="left:128px;top:26px;width:92px;height:42px;background:var(--grey-pale)"></div>
  <div class="brand"><span class="brand-square"></span><span class="brand-name">VELOQUARD</span></div>
  <div class="holder">
    <p class="holder-name">Daren Holt</p>
    <p class="holder-role">President</p>
  </div>
  <ul class="contact">
    <li><svg viewBox="0 0 10 10"><path d="M2 1l2 2-1 1.5c.8 1.5 1.5 2.2 3 3L7.5 6l2 2-1.5 1.5C4 9 1 6 .5 1.5z" fill="var(--cyan)"/></svg>888-8888-8888</li>
    <li><svg viewBox="0 0 10 10"><rect x="0" y="2" width="10" height="6" fill="var(--cyan)"/></svg>info@websitename.com</li>
    <li><svg viewBox="0 0 10 10"><circle cx="5" cy="5" r="4" fill="none" stroke="var(--cyan)" stroke-width="1.4"/></svg>www.websitename.com</li>
  </ul>
  <p class="address">55 demo street, demo place<br>P.O. Box 000, 555 Avenue</p>
</section>

<section class="sheet dark card-back" aria-label="Business card back">
  <div class="accent-block" style="left:13px;top:0;width:207px;height:56px;background:var(--slate)"></div>
  <div class="accent-block" style="left:13px;top:56px;width:207px;height:26px;background:var(--charcoal-tint)"></div>
  <div class="brand"><span class="brand-square"></span><span class="brand-name">VELOQUARD</span></div>
</section>

<section class="sheet paper envelope-back" aria-label="Envelope back">
  <svg class="envelope-flap" viewBox="0 0 339 50" preserveAspectRatio="none"><polygon points="0,0 339,0 319,50 22,50" fill="var(--charcoal-deep)"/></svg>
  <span class="brand-square"></span>
</section>

<section class="sheet paper envelope-front" aria-label="Envelope front">
  <div class="accent-block" style="left:137px;top:0;width:202px;height:31px;background:#e3f2fa"></div>
  <div class="accent-block" style="left:137px;top:31px;width:202px;height:123px;background:#f3f3f3"></div>
  <div class="brand"><span class="brand-square"></span><span class="brand-name">VELOQUARD</span></div>
  <p class="address">55 demo street, demo place<br>P.O. Box 000, 555 Avenue</p>
</section>

</body>
</html>
```